Book cover for book about ex-wifes

I need a book cover for my new book called "Tidligere brude fra Solen, Stormen og Lindevang" - In english: "Former brides from Sun, Storm and Lindevang" (Hørsholm is a posh city in Denmark).

The book is by men for men about ex-wifes and about how to avoid getting them.
Is it a book from a sexologist and couples therapist to men on how to improve relations.

Men (and curious women)

• Something that indicate three types of ex-wifes

And the author name “Jonas Beltoft”
• Something that says something about relationships, couples and how to stay together (or how to avoid not breaking up)
• No hate

```html
<!DOCTYPE html>
<html lang="da">
<head>
<meta charset="utf-8">
<title>Tidligere brude fra Solen, Stormen og Lindevang – Jonas Beltoft</title>
<link rel="stylesheet" href="https://fonts.googleapis.com/css2?family=Tinos:ital,wght@0,400;0,700;1,400&display=swap">
<style>
  :root {
    --night: #000000;
    --moon-light: #6a1690;
    --moon-mid: #551078;
    --moon-deep: #3a0a55;
    --house-shadow: #14061d;
    --author-violet: #d600f2;
    --title-white: #ffffff;
    --quote-grey: #9a9a9a;
  }
  * { margin: 0; padding: 0; box-sizing: border-box; }
  html, body {
    width: 846px;
    height: 1200px;
    overflow: hidden;
    background: var(--night);
  }
  .cover {
    position: relative;
    width: 846px;
    height: 1200px;
    background: var(--night);
    overflow: hidden;
    font-family: "Tinos", "Times New Roman", serif;
  }
  .cover-photo {
    position: absolute;
    inset: 0;
    width: 846px;
    height: 1200px;
  }
  .author {
    position: absolute;
    left: 70px;
    top: 172px;
    font-size: 56px;
    font-weight: 400;
    line-height: 1;
    color: var(--author-violet);
    letter-spacing: -0.5px;
  }
  .title {
    position: absolute;
    left: 74px;
    top: 250px;
    font-size: 92px;
    font-weight: 700;
    line-height: 96px;
    color: var(--title-white);
    letter-spacing: -2px;
  }
  .title span { display: block; }
  .epigraph {
    position: absolute;
    left: 470px;
    top: 982px;
    color: var(--quote-grey);
  }
  .epigraph-text {
    font-style: italic;
    font-size: 22px;
    line-height: 30px;
    transform: rotate(-1.5deg);
    transform-origin: left top;
  }
  .epigraph-source {
    margin-top: 14px;
    margin-left: 98px;
    font-size: 14px;
    letter-spacing: 3px;
    text-transform: uppercase;
    color: var(--author-violet);
  }
</style>
</head>
<body>
  <main class="cover">
    <svg class="cover-photo" viewBox="0 0 846 1200" role="img"
         aria-label="Photograph: a huge violet full moon rising behind silhouettes of people sitting and standing on grass at night, one looking at a phone, a faint house in the dark upper right">
      <defs>
        <radialGradient id="moonGlow" cx="50%" cy="45%" r="55%">
          <stop offset="0%" stop-color="var(--moon-light)"/>
          <stop offset="70%" stop-color="var(--moon-mid)"/>
          <stop offset="100%" stop-color="var(--moon-deep)"/>
        </radialGradient>
      </defs>
      <rect class="house-shadow" x="695" y="150" width="151" height="260" fill="var(--house-shadow)"/>
      <circle class="moon" cx="415" cy="705" r="363" fill="url(#moonGlow)"/>
      <rect class="ground" x="0" y="958" width="846" height="242" fill="var(--night)"/>
    </svg>

    <p class="author">Jonas Beltoft</p>

    <h1 class="title">
      <span>Tidligere brude</span>
      <span>fra Solen,</span>
      <span>Stormen og</span>
      <span>Lindevang</span>
    </h1>

    <figure class="epigraph">
      <blockquote class="epigraph-text">“There is no remedy<br>for love but to love more”</blockquote>
      <figcaption class="epigraph-source">Elias Marlowe</figcaption>
    </figure>
  </main>
</body>
</html>
```